Drone company needs a brochure design

We would like a brochure design which compliments our existing logo, website and business card designs.

www.bramblecrest.com.au

```html
<!DOCTYPE html>
<html lang="en">
<head>
<meta charset="utf-8">
<title>Bramblecrest Brochure Spread</title>
<link rel="stylesheet" href="https://fonts.googleapis.com/css2?family=Ubuntu:wght@400;500;700&display=swap">
<style>
  :root {
    --brand-blue: #0088c8;
    --brand-blue-veil: rgba(0, 128, 195, 0.72);
    --teal-band: rgba(0, 150, 180, 0.42);
    --paper: #ffffff;
    --ink: #2a3a4a;
    --white: #ffffff;
    --rule: #555f69;
  }
  * { margin: 0; padding: 0; box-sizing: border-box; }
  html, body { width: 1200px; height: 1200px; overflow: hidden; background: var(--paper); }
  body { position: relative; font-family: "Ubuntu", sans-serif; color: var(--ink); }

  .page-number { position: absolute; left: 952px; top: 22px; font-size: 9px; color: var(--ink); }

  .city-photo {
    position: absolute; left: 138px; top: 130px; width: 694px; height: 349px;
    background:
      linear-gradient(90deg, rgba(70,55,40,0.65) 0%, rgba(70,55,40,0) 22%, rgba(0,0,0,0) 70%, rgba(20,30,30,0.7) 100%),
      linear-gradient(180deg, #dfe6ea 0%, #b9b2a4 35%, #8d7a62 70%, #4d4033 100%);
  }
  .feature-panel {
    position: absolute; left: 581px; top: 174px; width: 421px; height: 262px;
    background: linear-gradient(90deg, var(--brand-blue-veil) 0, var(--brand-blue-veil) 251px, var(--brand-blue) 251px, var(--brand-blue) 100%);
    color: var(--white);
    padding: 36px 30px 0 39px;
  }
  .feature-title { font-size: 23px; font-weight: 400; line-height: 1; white-space: nowrap; }
  .feature-copy { margin-top: 44px; font-size: 12px; line-height: 15.3px; width: 345px; }
  .feature-copy p + p { margin-top: 15.3px; }

  .site-link {
    position: absolute; right: 242px; top: 561px; font-size: 9.5px; letter-spacing: 0.3px;
    color: var(--brand-blue);
  }
  .margin-rule { position: absolute; left: 1002px; top: 564px; width: 1px; height: 46px; background: var(--rule); }

  .skyline-photo {
    position: absolute; left: 138px; top: 610px; width: 864px; height: 564px; overflow: hidden;
    background:
      linear-gradient(180deg, #c9d3e6 0%, #9fb0cf 22%, #7e93b8 36%, #4a6a93 44%, #2b4868 58%, #1c2f44 78%, #2a3540 100%);
  }
  .teal-band { position: absolute; left: 0; top: 260px; width: 100%; height: 174px; background: var(--teal-band); }

  .directors { position: absolute; left: 182px; top: 899px; width: 362px; color: var(--white); }
  .directors-title { font-size: 23px; font-weight: 400; line-height: 1; white-space: nowrap; }
  .directors-sub { margin-top: 14px; font-size: 11.6px; line-height: 15.5px; }
  .directors-copy { font-size: 11.6px; line-height: 15.5px; }

  .assets { position: absolute; left: 725px; top: 899px; width: 240px; color: var(--white); }
  .assets-rule { width: 120px; height: 1px; background: var(--white); }
  .assets-title { margin-top: 6px; font-size: 13.5px; font-weight: 500; line-height: 15.5px; }
  .assets-copy { font-size: 11.6px; line-height: 15.5px; }

  .site-link-footer {
    position: absolute; left: 824px; top: 1125px; font-size: 9.5px; letter-spacing: 0.3px;
    color: var(--brand-blue); opacity: 0.75;
  }
</style>
</head>
<body>
  <div class="page-number">7</div>

  <section class="spread spread-inspection">
    <div class="city-photo" role="img" aria-label="Photo looking across tall city skyscrapers in warm daylight"></div>
    <div class="feature-panel">
      <h1 class="feature-title">INSPECTION &amp; ENVIRONMENT</h1>
      <div class="feature-copy">
        <p>We eliminate the need for expensive and time consuming scaf-folding, man-lifting equipment and helicopter chartersa.</p>
        <p>Our cameras can be viewed in real-time&nbsp; from the ground by your qualified technitians and we can take in-flight instructions in order to provide the perfect vantage for their specific needs.</p>
      </div>
    </div>
  </section>

  <div class="site-link">WWW.BRAMBLECREST.COM.AU</div>
  <div class="margin-rule"></div>

  <section class="spread spread-directors">
    <div class="skyline-photo" role="img" aria-label="Aerial photo of a sprawling city under a cloudy blue sky with a tall tower in the foreground">
      <div class="teal-band"></div>
    </div>

    <div class="directors">
      <h2 class="directors-title">BOARD OF DIRECTORS</h2>
      <p class="directors-sub">Strategic highlights</p>
      <p class="directors-copy">Estis et rerumendion con nisit vel ipiendu cillit fugit ut aut qui to ea que sero eos quo que porerciur aliti Facest qui que acepre non pa por reprae pro corit, audamusam faccum aut officab ipsant venis autem fuga. Incid quam idesequam autatet ea parisin cimenihilis.</p>
    </div>

    <div class="assets">
      <div class="assets-rule"></div>
      <h3 class="assets-title">Our mobile assets</h3>
      <p class="assets-copy">Comnisit anducid qui il inveni ut plibusam harum eum, to consed quiae verspel iquiam, et, simos nonsequ idenectur.</p>
    </div>

    <div class="site-link-footer">WWW.BRAMBLECREST.COM.AU</div>
  </section>
</body>
</html>
```